a residential cleaning service needs a website

We need a website for our faith based residential cleaning service, we are called MARGOT'S CLEANING SERVICE. We want a website that is clean looking both for mobile version and desktop. We want to convey cleanliness and trust to our clients. The color scheme should go in hand with the colors of the LOGO. We would like an about page, statement of faith page, services page and also a page for a booking module that our CRM has provided for us to being able to code and dress said module is important. The website not only needs to market to new customers and convey our service but also be easy to use for existing clients to schedule cleanings and services.
Industry/Entity Type
Cleaning Service
Coding
Coded - Design and coding required
Number of Pages Required
4 page
Requirements
Must have
- About page
Statement of Faith page
services page
booking and login page

```html
<!DOCTYPE html>
<html lang="en">
<head>
<meta charset="utf-8">
<title>Margot's Cleaning Service</title>
<link href="https://fonts.googleapis.com/css2?family=Roboto:wght@400;500;700&family=Roboto+Condensed:wght@400;700&display=swap" rel="stylesheet">
<style>
:root{
  --accent:#1fb3e6;
  --navy:#2b4a93;
  --navy-dark:#233f80;
  --ink:#2b2b2b;
  --body:#444;
  --muted:#777;
  --line:#e6e6e6;
  --white:#fff;
}
*{margin:0;padding:0;box-sizing:border-box}
html,body{width:1200px;height:998px;overflow:hidden;background:var(--white)}
body{font-family:"Roboto",sans-serif;color:var(--body);position:relative}

.topbar{position:absolute;left:0;top:0;width:1200px;height:40px;border-top:3px solid var(--accent);border-bottom:1px solid var(--line)}
.topbar .cell{position:absolute;top:0;height:36px;border-left:1px solid var(--line);display:flex;align-items:center;font-size:7.6px;color:var(--muted)}
.tagline{left:232px;width:233px;padding-left:15px;border-right:1px solid var(--line)}
.social{left:546px;gap:14px;border:none!important}
.social span{width:8px;height:8px;border-radius:50%;background:#c4c4c4;display:block}
.phone{left:761px;width:95px;padding-left:18px}
.mail{left:856px;width:113px;padding-left:18px;border-right:1px solid var(--line)}
.topbar svg{margin-right:5px}

.navbar{position:absolute;left:0;top:40px;width:1200px;height:68px}
.nav{position:absolute;right:232px;top:26px;display:flex;gap:17px;list-style:none;font-size:9.4px;color:var(--ink);letter-spacing:.2px}
.nav .active{color:var(--navy)}

.brand{position:absolute;left:214px;top:39px;width:122px;height:122px;border-radius:50%;background:var(--white);z-index:3;display:flex;align-items:center;justify-content:center;text-align:center;font-family:"Roboto Condensed",sans-serif;font-weight:700;color:var(--navy);font-size:11px;line-height:1.25;padding-top:4px}

.hero{position:absolute;left:0;top:107px;width:1200px;height:540px;overflow:hidden}
.hero-photo{position:absolute;inset:0;background:
  radial-gradient(ellipse 260px 220px at 700px 420px,#3f86d6 0%,rgba(63,134,214,0) 100%),
  radial-gradient(ellipse 200px 240px at 380px 360px,#e87a2a 0%,rgba(232,122,42,0) 100%),
  radial-gradient(ellipse 220px 200px at 950px 230px,#e8c53a 0%,rgba(232,197,58,0) 100%),
  linear-gradient(90deg,#cfb89a 0%,#c9a86a 30%,#d7d2c8 55%,#7f9fc2 80%,#5b7da3 100%)}
.hero-copy{position:absolute;left:231px;top:171px;color:var(--white)}
.hero-title{font-family:"Roboto Condensed",sans-serif;font-weight:700;font-size:29px;line-height:32px;text-transform:uppercase}
.hero-text{margin-top:20px;width:320px;font-size:8.8px;line-height:15px}
.btn-light{display:inline-block;margin-top:29px;width:96px;height:34px;line-height:32px;text-align:center;background:var(--white);color:var(--navy);font-weight:700;font-size:8.8px;border-bottom:3px solid var(--navy)}
.wave{position:absolute;left:0;bottom:0;width:1200px;height:8px}

.welcome{position:absolute;left:213px;top:703px;width:290px}
.eyebrow{font-size:12.5px;color:#555;font-weight:400}
.welcome h1{font-family:"Roboto",sans-serif;font-size:16px;font-weight:500;color:var(--ink);margin-top:4px}
.welcome p{margin-top:16px;font-size:9.3px;line-height:13.8px;color:var(--body)}
.welcome p+p{margin-top:9px}
.btn-solid{position:absolute;left:-1px;top:221px;width:82px;height:34px;line-height:32px;text-align:center;background:var(--navy);color:var(--white);font-weight:700;font-size:8.8px;border-bottom:3px solid #3e84d8}

.feature{position:absolute;width:240px}
.feature .badge{position:absolute;left:0;top:0;width:39px;height:49px}
.feature h3{position:absolute;left:56px;top:5px;font-family:"Roboto Condensed",sans-serif;font-weight:700;font-size:10px;color:var(--ink);white-space:nowrap}
.feature p{position:absolute;left:56px;top:24px;width:160px;font-size:8px;line-height:13.8px;color:#555}
</style>
</head>
<body>

<header class="topbar">
  <div class="cell tagline">PROFESSIONAL CLEANING SERVICES YOU CAN TRUST</div>
  <div class="cell social" aria-label="Social links"><span></span><span></span><span></span><span></span><span></span></div>
  <div class="cell phone"><svg width="8" height="8" viewBox="0 0 8 8"><rect width="8" height="8" rx="1.5" fill="#1fb3e6"/><path d="M2.3 1.8l1 1-.5.6a3 3 0 0 0 1.8 1.8l.6-.5 1 1-.6.7C3.8 6.2 1.8 4.2 1.6 2.4z" fill="#fff"/></svg>0800-555010</div>
  <div class="cell mail"><svg width="8" height="8" viewBox="0 0 8 8"><rect width="8" height="8" rx="1.5" fill="#1fb3e6"/><rect x="1.6" y="2.3" width="4.8" height="3.4" fill="#fff"/><path d="M1.6 2.3L4 4.3 6.4 2.3" stroke="#1fb3e6" stroke-width=".6" fill="none"/></svg>hello@margotsclean.example</div>
</header>

<nav class="navbar">
  <ul class="nav">
    <li class="active">HOME</li><li>ABOUT</li><li>SERVICES</li><li>PRICING</li><li>BLOG</li><li>TESTIMONIALS</li><li>CONTACT US</li>
  </ul>
</nav>

<div class="brand">MARGOT'S<br>CLEANING<br>SERVICE</div>

<section class="hero">
  <div class="hero-photo" role="img" aria-label="Photo of cleaning supplies: spray bottles, detergent jugs, orange rubber gloves and a cloth in a blue bucket"></div>
  <div class="hero-copy">
    <h2 class="hero-title">Using only the best<br>products</h2>
    <p class="hero-text">Abitant morbi tristique senectus eft netus eft malesuada fames ac turpis egestas enean non tell. Donec pede quam placerat ristique faucibus poserw uete lobortid Lorem ipsum dolor sit amet consectetur.</p>
    <span class="btn-light">HOW WE DO IT</span>
  </div>
  <svg class="wave" viewBox="0 0 1200 8" preserveAspectRatio="none">
    <defs><pattern id="scallop" width="16" height="8" patternUnits="userSpaceOnUse"><path d="M0 4Q4 1 8 3.5T16 4V8H0Z" fill="#fff"/></pattern></defs>
    <rect width="1200" height="8" fill="url(#scallop)"/>
  </svg>
</section>

<section class="welcome">
  <div class="eyebrow">WELCOME TO</div>
  <h1>MARGOT'S CLEANING SERVICE</h1>
  <p>Margot's Cleaning Service is a faith based cleaning business founded in middle Tennessee over 19 years ago. Fueled by great work and word of mouth, a part time source of income to a mother of 4 changed and grew by into a full time job. Over the years Margot's Cleaning Service has developed its cleaning process into a methodical approach where attention to detail and a continual striving for excellence presents itself in everything we do.</p>
  <p>We realize that life gets busy and sometimes cleaning is a tall hurdle to overcome, so we consider it an honor if we get to help make life a little easier.</p>
  <span class="btn-solid">READ MORE</span>
</section>

<div class="feature" style="left:521px;top:765px">
  <svg class="badge" viewBox="0 0 39 49"><path d="M.5 .5H38.5V40L19.5 48.5.5 40Z" fill="#fff" stroke="#e2e2e2"/><circle cx="19.5" cy="21" r="8" fill="none" stroke="#444" stroke-width="2"/><circle cx="19.5" cy="21" r="3.5" fill="none" stroke="#444" stroke-width="2"/><path d="M14 15.5l3 3M25 15.5l-3 3M14 26.5l3-3M25 26.5l-3-3" stroke="#444" stroke-width="2"/></svg>
  <h3>FLEXIBLE CLEANING PLANS</h3>
  <p>Aenean non tell us. Donec pede quam plac erat faucibus lobortis justo.</p>
</div>
<div class="feature" style="left:763px;top:765px">
  <svg class="badge" viewBox="0 0 39 49"><path d="M.5 .5H38.5V40L19.5 48.5.5 40Z" fill="#fff" stroke="#e2e2e2"/><circle cx="19.5" cy="16" r="4.5" fill="#444"/><path d="M11.5 30a8 7 0 0 1 16 0z" fill="#444"/></svg>
  <h3>VERIFIED EMPLOYEES</h3>
  <p>Aenean non tell us. Donec pede quam plac erat faucibus lobortis justo.</p>
</div>
<div class="feature" style="left:521px;top:852px">
  <svg class="badge" viewBox="0 0 39 49"><path d="M0 0H39V40L19.5 49 0 40Z" fill="#2b4a93"/><path d="M12 28C12 18 20 13 28 13 28 22 22 28 14 27M12 28L22 19" fill="#fff" stroke="#fff" stroke-width="1.2"/><path d="M13 27l9-8" stroke="#2b4a93" stroke-width="1.2"/></svg>
  <h3>GREEN CLEANING SOLUTIONS</h3>
  <p>Aenean non tell us. Donec pede quam plac erat faucibus lobortis justo.</p>
</div>
<div class="feature" style="left:763px;top:852px">
  <svg class="badge" viewBox="0 0 39 49"><path d="M.5 .5H38.5V40L19.5 48.5.5 40Z" fill="#fff" stroke="#e2e2e2"/><path d="M9.5 21a10 8 0 0 1 20 0z" fill="#444"/><path d="M19.5 21v7a2 2 0 0 1-4 0" stroke="#444" stroke-width="1.8" fill="none"/></svg>
  <h3>BEST CUSTOMER SUPPORT</h3>
  <p>Aenean non tell us. Donec pede quam plac erat faucibus lobortis justo.</p>
</div>

</body>
</html>
```